Do it yourself Karten und Hochzeitsdeko selbstgemacht
Zielgruppe
Wir sind ein Bastelgeschäft. Wir bieten Materialien zum selber machen von Karten, Tischkarten,Menükarten, Gästebüchern, Fotoalben an.
Alle Materialien zur Anlassgestaltung, auch Tischdeko und Kerzen.
Zielgruppe: Junge Leute auf einer Hochzeitsmesse
Aufgabenstellung
Ich benötige einen Flyer in A5 Format. Einige Fotoausschnitte und Text. Romantisch.
Fotos von angefertigten Karten und Deko sind vorhanden.
Logo vorhanden, soll mit rein und Öffnungszeiten mit Internet
Text: Do it Yourself Karten und Hochzeitsdeko selbst gemacht!
Zeiten etc. bitte www.falten-und-schmuecken.de

```html
<!DOCTYPE html>
<html lang="de">
<head>
<meta charset="utf-8">
<title>Do it yourself – Karten &amp; Hochzeitsdeko selbstgemacht</title>
<link rel="stylesheet" href="https://fonts.googleapis.com/css2?family=Dancing+Script:wght@400;600&family=Raleway:wght@300;400&display=swap">
<style>
:root{
  --teal:#4a979e;
  --teal-dark:#2e6a6d;
  --paper:#ffffff;
  --ink:#1d1d1d;
  --ink-soft:#3a3a3a;
  --bg-top:#f4f4f4;
  --bg-bottom:#a9a9a9;
  --photo-light:#c9cdd6;
  --photo-mid:#8f96a6;
}
*{margin:0;padding:0;box-sizing:border-box}
html,body{width:1200px;height:810px;overflow:hidden}
body{background:linear-gradient(var(--bg-top),var(--bg-bottom));position:relative;font-family:"Dancing Script",cursive}
.page{position:absolute;top:24px;width:529px;height:749px;background:var(--paper);overflow:hidden;box-shadow:0 2px 8px rgba(0,0,0,.25)}
.page--front{left:44px}
.page--back{left:612px}
.bands{position:absolute;inset:0}
.headline{position:absolute;left:0;right:0;top:28px;text-align:center;color:#fff;font-size:48px;line-height:50px;font-weight:400;text-shadow:1px 2px 3px rgba(0,0,0,.55)}
.photo{position:absolute;box-shadow:0 1px 4px rgba(0,0,0,.35)}
.photo--hero{left:41px;top:202px;width:443px;height:296px;background:linear-gradient(135deg,#e8eaf0,var(--photo-light) 45%,var(--photo-mid))}
.photo--inset{left:345px;top:350px;width:150px;height:150px;border-radius:50%;background:radial-gradient(circle,#3f5a3a 25%,#e9e9ec 55%,#cfd1d6);box-shadow:0 1px 6px rgba(0,0,0,.4)}
.brand{position:absolute;left:56px;top:216px;display:flex;align-items:center;gap:8px}
.brand__mark{width:10px;height:10px;background:var(--teal-dark)}
.brand__name{font-family:"Raleway",sans-serif;font-weight:400;font-size:18px;color:var(--teal-dark);letter-spacing:.5px}
.invite{position:absolute;left:0;right:0;top:542px;text-align:center;color:var(--ink);font-size:25px;line-height:28px;font-weight:600}
.offer{position:absolute;left:0;right:0;top:624px;text-align:center;color:var(--ink-soft);font-size:20px;line-height:24px}
.range{position:absolute;left:0;right:0;top:20px;text-align:center;color:var(--ink-soft);font-size:19.5px;line-height:24px}
.range p+p{margin-top:24px}
.photo--menu{left:41px;top:301px;width:218px;height:327px;background:linear-gradient(160deg,#6d7480,#d6d8de 45%,#8a8f99)}
.photo--table{left:267px;top:301px;width:218px;height:327px;background:linear-gradient(170deg,#5e5c56,#cfcfd2 50%,#7f837f)}
.contact{position:absolute;top:662px;font-family:"Raleway",sans-serif;font-weight:300;font-size:12px;line-height:15px;color:#fff;font-style:normal}
.contact--address{left:50px}
.contact--hours{left:277px}
.contact--hours .gap{height:15px}
</style>
</head>
<body>

<section class="page page--front">
  <svg class="bands" width="529" height="749" aria-hidden="true">
    <polygon points="0,0 529,0 529,190 0,366" fill="var(--teal-dark)"/>
    <polygon points="0,0 529,0 529,104 0,352" fill="var(--teal)"/>
  </svg>
  <h1 class="headline">Do it yourself<br>Karten &amp; Hochzeitsdeko<br>selbstgemacht</h1>
  <div class="photo photo--hero" role="img" aria-label="Foto: weiße Gastgeschenk-Schachteln mit Aufschrift „Wir heiraten – Reis, bitte streuen!“ zwischen Reiskörnern"></div>
  <div class="photo photo--inset" role="img" aria-label="Foto: Ringkissen mit Herz aus Buchsbaum und weißer Schleife"></div>
  <div class="brand"><span class="brand__mark"></span><span class="brand__name">Hansen</span></div>
  <p class="invite">Wir würden uns freuen, Sie bei der Gestaltung Ihrer<br>ganz persönlichen Einladungskarte beraten zu dürfen!!!</p>
  <p class="offer">In unseren Räumen finden Sie Herziges und Glückbringendes,<br>Brautpaare, Tauben, Ringkissen,<br>Fotoalben, Gästebücher, Kerzen und Servietten.</p>
</section>

<section class="page page--back">
  <svg class="bands" width="529" height="749" aria-hidden="true">
    <polygon points="0,622 529,432 529,749 0,749" fill="var(--teal-dark)"/>
    <polygon points="0,636 529,452 529,749 0,749" fill="var(--teal)"/>
  </svg>
  <div class="range">
    <p>Eine Auswahl verschiedenster Papiere und Stempel,<br>zur Kartengestaltung für Hochzeit, Taufe, Konfirmation,<br>Geburtstag und sonstige Anlässe.<br>Wachsplatten und Stifte zum Kerzenverzieren.</p>
    <p>Verschiedene Variationen von Bändern, Kordeln<br>und Tüll für Kirchendekorationen und Autoschmuck.</p>
    <p>Glas- und Wachsperlen, Pailetten, Rocailles und Indianerperlen,<br>Strasssteine und Funkelkristalle, Drähte, Verschlüsse und<br>Bänder zur Schmuckgestaltung.</p>
  </div>
  <div class="photo photo--menu" role="img" aria-label="Foto: selbstgestaltete Menükarte mit Spitzenherz neben einem Weinglas"></div>
  <div class="photo photo--table" role="img" aria-label="Foto: Tischdeko mit Karten, Herzanhängern, Windlichtern und Kerzengläsern"></div>
  <address class="contact contact--address">
    Hansen Basteln und Dekorieren<br>
    Lindenweg 12<br>
    21400 Elbstedt<br>
    Tel.: 04100 - 12 34 56
  </address>
  <div class="contact contact--hours">
    Öffnungszeiten:
    <div class="gap"></div>
    Montag-Samstag: 09.30-13.00 Uhr<br>
    Mo, Di, Do &amp; Fr: 14.30-18.00 Uhr
  </div>
</section>

</body>
</html>
```